July 15 Raffle Fundraiser to raise $2000

Fundraiser for the family to travel to Halifax NB and support athlete Corvel Ashbury.
Travel dates: July 16-23,2023

Raffling off three prizes
1) $150.00 Firewood
2) $375.00 Red Safe
3) $300.00 Secure Latch and door knob
4) 20 pieces of frozen coho sockeye

Tickets are
$2.00 each
$5.00 for three

Draw Date: July 15,2023 @11:00am

Please help us raise $2000.00
To alleviate travelling and meal costs
ETransfer: ashburyfundraiser482@plimvex.com

I have included the pervious flyer we used
Information on there as well
And please try keep same Color scheme

Thanks

Target Market(s)

Athlete supporters

Colors

Designer to choose colors to be used in the design.

Requirements
Must have
• Pictures of the raffle items , with exception of the fish there no picture of fish
Nice to have
• Pictures of the athlete in a minimal way. Similar to the colours and design of previous flyer to stay consistent. But fine if it is different.

```html
<!DOCTYPE html>
<html lang="en">
<head>
<meta charset="utf-8">
<title>Loonie Twoonie Fundraiser</title>
<link href="https://fonts.googleapis.com/css2?family=Alfa+Slab+One&family=Montserrat:wght@500;600;700;800&display=swap" rel="stylesheet">
<style>
  :root {
    --navy: #173f8e;
    --blue: #1d55b6;
    --blue-text: #1f4fae;
    --yellow: #f8e61b;
    --gold: #f6c400;
    --title-gold: #f3c21c;
    --grey-band: #ececec;
    --ink: #1b1b1b;
    --white: #ffffff;
    --muted: #c9d6f2;
  }
  * { margin: 0; padding: 0; box-sizing: border-box; }
  html, body { width: 848px; height: 1200px; overflow: hidden; background: var(--white); }
  body { font-family: "Montserrat", Arial, sans-serif; color: var(--ink); }
  .flyer { position: relative; width: 848px; height: 1200px; overflow: hidden; background: var(--white); }
  .athlete-photo {
    position: absolute; left: 0; top: 0; width: 848px; height: 480px;
    background: linear-gradient(180deg, #9dcbe0 0%, #79b2ca 55%, #4f86a0 100%);
  }
  .shapes { position: absolute; left: 0; top: 0; width: 848px; height: 1200px; }
  .t { position: absolute; white-space: nowrap; line-height: 1; }

  .brand { right: 44px; top: 128px; font-weight: 800; font-size: 24px; color: var(--navy); letter-spacing: .5px; display: flex; align-items: center; gap: 8px; }
  .brand-dot { width: 14px; height: 14px; border-radius: 50%; background: var(--gold); display: inline-block; }

  .title { left: 34px; top: 326px; font-family: "Alfa Slab One", Georgia, serif; font-size: 41px; color: var(--white); line-height: 1.1; }
  .title span { color: var(--title-gold); display: block; }
  .title-rule { position: absolute; left: 34px; top: 436px; width: 278px; height: 2px; background: var(--muted); }
  .travel-label { left: 34px; top: 460px; font-size: 19px; font-weight: 500; color: var(--white); }
  .travel-dates { left: 32px; top: 483px; font-size: 42px; font-weight: 700; color: var(--white); }

  .goal-lead { left: 474px; top: 510px; font-size: 29px; font-weight: 600; color: var(--ink); }
  .goal-amount { left: 472px; top: 559px; font-size: 48px; font-weight: 800; color: var(--ink); }

  .purpose { left: 415px; top: 661px; font-size: 19px; font-weight: 500; color: var(--white); }
  .draw-icon { position: absolute; left: 478px; top: 720px; width: 32px; height: 34px; }
  .draw-label { left: 537px; top: 716px; font-size: 21px; font-weight: 500; color: var(--muted); }
  .draw-date { left: 536px; top: 748px; font-size: 36px; font-weight: 700; color: var(--yellow); }
  .draw-time { left: 536px; top: 796px; font-size: 36px; font-weight: 700; color: var(--white); }

  .prizes-heading { left: 30px; top: 604px; font-size: 22px; font-weight: 700; color: var(--ink); }
  .prize-list { position: absolute; left: 36px; top: 666px; list-style: none; }
  .prize-list li { position: relative; padding-left: 30px; font-size: 19.5px; font-weight: 500; line-height: 1.35; margin-bottom: 10px; }
  .prize-list b { color: var(--blue-text); font-weight: 700; }
  .prize-num { position: absolute; left: 0; top: 5px; width: 17px; height: 17px; border-radius: 50%; background: var(--gold); font-size: 10px; font-weight: 700; color: var(--ink); display: flex; align-items: center; justify-content: center; }
  .prize-rule { position: absolute; left: 30px; top: 860px; width: 392px; height: 3px; background: var(--navy); }

  .extras { position: absolute; left: 30px; top: 890px; }
  .extras p { font-size: 22px; font-weight: 700; line-height: 1.5; }
  .extras .coffee { color: var(--ink); }
  .extras .baked { color: var(--blue-text); }
  .extras .available { font-size: 20px; font-weight: 500; margin-top: 4px; }

  .won-list { position: absolute; left: 490px; top: 862px; list-style: none; }
  .won-list li { position: relative; padding-left: 30px; font-size: 17.5px; font-weight: 500; line-height: 1.5; margin-bottom: 16px; }
  .won-num { position: absolute; left: 0; top: 1px; width: 24px; height: 24px; border-radius: 50%; border: 2px solid var(--gold); color: var(--blue-text); font-size: 13px; font-weight: 700; display: flex; align-items: center; justify-content: center; }

  .tickets-label { left: 46px; top: 1042px; font-size: 19px; font-weight: 600; color: var(--white); }
  .tickets-price { left: 46px; top: 1076px; font-size: 32px; font-weight: 700; color: var(--gold); line-height: 1.45; }

  .etransfer { left: 340px; top: 1107px; font-size: 17.5px; font-weight: 500; color: var(--ink); }
  .etransfer b { font-weight: 700; }
</style>
</head>
<body>
<main class="flyer">
  <div class="athlete-photo" role="img" aria-label="Photo of the athlete playing basketball in a school gym"></div>

  <svg class="shapes" viewBox="0 0 848 1200" aria-hidden="true">
    <polygon points="0,296 400,296 470,400 424,570 0,570" fill="var(--navy)"/>
    <polygon points="0,570 424,570 394,651 0,651" fill="var(--grey-band)"/>
    <polygon points="469,400 406,480 522,480" fill="var(--gold)"/>
    <polygon points="406,480 848,480 848,626 438,626" fill="var(--yellow)"/>
    <polygon points="402,626 848,626 848,856 476,856 398,660" fill="var(--blue)"/>
    <polygon points="0,1021 370,1021 505,1179 0,1179" fill="var(--navy)"/>
    <polygon points="286,1085 848,1085 848,1152 345,1152" fill="var(--gold)"/>
  </svg>

  <div class="t brand"><span class="brand-dot"></span>TEAM KESTRA</div>

  <h1 class="t title">Loonie Twoonie<span>Fundraiser</span></h1>
  <div class="title-rule"></div>
  <p class="t travel-label">Travel dates:</p>
  <p class="t travel-dates">July 16-23,2023</p>

  <p class="t goal-lead">Please help us raise</p>
  <p class="t goal-amount">$2000.00</p>

  <p class="t purpose">(To alleviate travelling and meal costs)</p>
  <svg class="draw-icon" viewBox="0 0 32 34" fill="none" stroke="#dfe7f7" stroke-width="2">
    <rect x="2" y="5" width="24" height="23" rx="3"/>
    <line x1="8" y1="2" x2="8" y2="8"/><line x1="20" y1="2" x2="20" y2="8"/>
    <line x1="2" y1="12" x2="26" y2="12"/>
    <circle cx="23" cy="26" r="6" fill="var(--blue)"/>
    <polyline points="23,23 23,26 25,27"/>
  </svg>
  <p class="t draw-label">Draw Date:</p>
  <p class="t draw-date">July 15,2023</p>
  <p class="t draw-time">11:00am</p>

  <h2 class="t prizes-heading">Raffling off three prizes:</h2>
  <ol class="prize-list">
    <li><span class="prize-num">1</span><b>$150.00</b> Firewood</li>
    <li><span class="prize-num">2</span><b>$375.00</b> Red Safe</li>
    <li><span class="prize-num">3</span><b>$300.00</b> Secure Latch and<br>door knob</li>
    <li><span class="prize-num">4</span><b>20 pieces</b> of frozen coho sockeye</li>
  </ol>
  <div class="prize-rule"></div>

  <div class="extras">
    <p class="coffee">Coffee Provided</p>
    <p class="baked">Backed goods for sale</p>
    <p class="available">Items Currently Available to be won</p>
  </div>

  <ol class="won-list">
    <li><span class="won-num">1</span>Iawan chair/ fan/ and cooler</li>
    <li><span class="won-num">2</span>1 year Pricemark Membership</li>
    <li><span class="won-num">3</span>Fun Outdoor Games We will<br>have more once<br>June 24th arrives</li>
  </ol>

  <p class="t tickets-label">Tickets are</p>
  <p class="t tickets-price">$2.00 each<br>$5.00 for three</p>

  <p class="t etransfer">ETransfer: <b>ashburyfundraiser482@plimvex.com</b></p>
</main>
</body>
</html>
```